3.5" x 11" Door Hanger Design - Residential Roofing Company

We are looking for a double-sided door hanger that we can hang on the doors of prospects. This door hanger would have some brief information about our company, a phone number, website, and then the services that we offer. I don't know that it will have enough room for a lot of pictures, but feel free to use those from the marketing brochure if you think it'll work and I can get you the original as needed.
I have uploaded our certifications, logo, and then our current marketing brochure. The design should be cohesive with our marketing brochure, but doesn't have to match it perfectly.
Lastly, attached is the template that we are planning to print off of. This has a tear off portion at the bottom for a business card for a sales rep. The size of the overall door hanger will be 3.5" x 11", with the bottom 2.5" being the tear off business card with the salesman's information. I'll get you the sales reps information during the final design phase, but we will need name, title, phone number, email, business address, business website, list of services, and then the words "AZ ROC 562071" all on that small portion as well so if they tear it off they still have all the info.

```html
<!DOCTYPE html>
<html lang="en">
<head>
<meta charset="UTF-8">
<title>Granite Ridge Roofing – Door Hanger</title>
<link href="https://fonts.googleapis.com/css2?family=Poppins:wght@300;400;500;600;700&display=swap" rel="stylesheet">
<style>
  :root{
    --bg:#dcdcdc;
    --ink:#161616;
    --white:#ffffff;
    --orange:#f2561d;
    --muted:#e6e6e6;
    --faint:#f1f1f1;
    --badge-green:#1f9a4a;
    --badge-blue:#23408e;
  }
  *{margin:0;padding:0;box-sizing:border-box}
  html,body{width:1200px;height:1148px;overflow:hidden;background:var(--bg)}
  body{position:relative;font-family:"Poppins",sans-serif;color:var(--white)}
  .hanger{position:absolute;top:89px;width:320px;height:970px;background:var(--ink);overflow:hidden}
  .hanger--front{left:230px}
  .hanger--back{left:620px}
  .photo{position:absolute;left:0;top:0;width:320px;height:380px}
  .photo--house{background:linear-gradient(180deg,#8d929b 0%,#b7bbc2 35%,#7d7a74 60%,#5c5a57 78%,#8b8882 100%)}
  .photo--crew{background:linear-gradient(180deg,#5c8fcf 0%,#9cbbe0 22%,#5d5a58 45%,#3a3634 70%,#2a2725 100%)}
  .roofline{position:absolute;left:0;top:0;width:320px;height:420px}
  .hole{position:absolute;left:0;top:0;width:320px;height:170px}
  .card-stub{position:absolute;left:0;top:798px;width:320px;height:172px;background:var(--white)}
  .card-stub span{position:absolute;left:0;right:0;top:78px;text-align:center;font-size:19px;font-weight:600;color:var(--faint)}
  .brand{position:absolute;display:flex;align-items:center;gap:6px;font-size:15px;font-weight:600;color:var(--white);white-space:nowrap}
  .brand i{display:block;width:10px;height:10px;background:var(--orange)}
  .brand--front{left:16px;top:316px}
  .brand--back{right:14px;top:324px;font-size:14px}
  .t{position:absolute;left:18px;right:16px}
  .headline{top:368px;font-size:28px;font-weight:300;line-height:1.15}
  .headline b{color:var(--orange);font-weight:600}
  .headline strong{color:var(--orange);font-weight:700}
  .lead{top:443px;font-size:9.4px;font-weight:600;line-height:1.4}
  .subhead{top:491px;font-size:13px;font-weight:600;color:var(--orange)}
  .body{top:514px;font-size:9.4px;line-height:1.45;color:var(--muted)}
  .checks{position:absolute;left:18px;right:14px;top:571px;list-style:none}
  .checks li{display:flex;gap:8px;font-size:9.2px;line-height:1.45;color:var(--muted);height:40px}
  .checks svg{flex:0 0 12px;margin-top:2px}
  .phone-pill{position:absolute;left:62px;top:731px;width:186px;height:30px;border-radius:15px;background:var(--orange);display:flex;align-items:center;justify-content:center;gap:8px;font-size:17px;font-weight:600}
  .web{position:absolute;left:0;right:0;top:772px;text-align:center;font-size:9.6px;font-weight:600}
  .back-title{top:384px;font-size:27px;font-weight:600;line-height:1.22}
  .intro{top:466px;font-size:9.4px;line-height:1.45;color:var(--muted)}
  .services{position:absolute;left:16px;right:12px;top:508px;list-style:none}
  .services li{display:flex;gap:10px;height:41px;font-size:9.4px;line-height:1.45;color:var(--muted)}
  .services b{color:var(--orange);font-weight:600}
  .ico{flex:0 0 22px;width:22px;height:22px;border-radius:50%;background:var(--orange);display:flex;align-items:center;justify-content:center}
  .contact-title{top:667px;font-size:13px;font-weight:600}
  .contact{position:absolute;left:18px;display:flex;align-items:center;gap:8px;font-size:9px;font-weight:500}
  .badges{position:absolute;left:18px;top:748px;display:flex;align-items:center;gap:12px}
  .badge-round{width:30px;height:30px;border-radius:50%;background:var(--badge-green);border:2px solid var(--white)}
  .badge-square{width:22px;height:26px;background:var(--badge-blue);border-bottom:6px solid #c22a2a}
  .roc{font-size:7px;font-weight:500;margin-left:12px}
</style>
</head>
<body>

<section class="hanger hanger--front">
  <div class="photo photo--house" role="img" aria-label="Photo of a single-storey stone and wood home under a cloudy sky"></div>
  <svg class="roofline" viewBox="0 0 320 420" aria-hidden="true">
    <polygon points="190,318 222,300 320,300 320,348" fill="var(--orange)"/>
    <polygon points="0,262 42,238 320,338 320,352 42,252 0,276" fill="var(--white)"/>
    <polygon points="0,276 42,252 320,352 320,420 0,420" fill="var(--ink)"/>
  </svg>
  <svg class="hole" viewBox="0 0 320 170" aria-hidden="true">
    <polygon points="150,0 200,0 190,40 160,40" fill="var(--bg)"/>
    <circle cx="164" cy="81" r="72" fill="var(--bg)"/>
  </svg>

  <div class="brand brand--front"><i></i>Granite Ridge Roofing</div>
  <h1 class="t headline">Quality <b>Roofing</b><br>you can <strong>trust</strong></h1>
  <p class="t lead">Avoid costly repairs by catching issues early. Ensure your roof's integrity with a professional inspection.</p>
  <h2 class="t subhead">Why Regular Roof Inspections Matter</h2>
  <p class="t body">A well-maintained roof protects your home, saves you money, and extends its lifespan. Our expert roof checkups help:</p>
  <ul class="checks">
    <li><svg width="12" height="12" viewBox="0 0 12 12"><circle cx="6" cy="6" r="6" fill="var(--orange)"/><path d="M3.2 6.2l1.8 1.8 3.8-4" stroke="#fff" stroke-width="1.4" fill="none"/></svg><span>Identify Hidden Damage – Catch minor issues before they become major problems.</span></li>
    <li><svg width="12" height="12" viewBox="0 0 12 12"><circle cx="6" cy="6" r="6" fill="var(--orange)"/><path d="M3.2 6.2l1.8 1.8 3.8-4" stroke="#fff" stroke-width="1.4" fill="none"/></svg><span>Prevent Costly Repairs – Addressing small repairs now can save thousands in the future.</span></li>
    <li><svg width="12" height="12" viewBox="0 0 12 12"><circle cx="6" cy="6" r="6" fill="var(--orange)"/><path d="M3.2 6.2l1.8 1.8 3.8-4" stroke="#fff" stroke-width="1.4" fill="none"/></svg><span>Improve Energy Efficiency – A well-maintained roof helps regulate indoor temperatures.</span></li>
    <li><svg width="12" height="12" viewBox="0 0 12 12"><circle cx="6" cy="6" r="6" fill="var(--orange)"/><path d="M3.2 6.2l1.8 1.8 3.8-4" stroke="#fff" stroke-width="1.4" fill="none"/></svg><span>Prolong Roof Life – Routine checkups ensure your roof stays in top condition for years to come.</span></li>
  </ul>
  <div class="phone-pill">
    <svg width="18" height="18" viewBox="0 0 18 18" aria-hidden="true"><circle cx="9" cy="9" r="9" fill="#fff"/><path d="M6.2 4.6l1.6 2-0.9 1.2c.6 1.3 1.6 2.3 2.9 2.9l1.2-.9 2 1.6-.8 1.6c-3.6-.3-6.9-3.6-7.2-7.2z" fill="var(--orange)"/></svg>
    (928) 555-0147
  </div>
  <p class="web">www.graniteridgeroofing.com</p>

  <div class="card-stub"><span>Business card</span></div>
</section>

<section class="hanger hanger--back">
  <div class="photo photo--crew" role="img" aria-label="Photo of a roofing crew in safety harnesses installing shingles on a roof"></div>
  <svg class="roofline" viewBox="0 0 320 420" aria-hidden="true">
    <polygon points="0,300 118,292 140,306 0,346" fill="var(--orange)"/>
    <polygon points="0,348 160,260 320,302 320,316 160,274 0,362" fill="var(--white)"/>
    <polygon points="0,362 160,274 320,316 320,420 0,420" fill="var(--ink)"/>
  </svg>
  <svg class="hole" viewBox="0 0 320 170" aria-hidden="true">
    <polygon points="150,0 200,0 190,40 160,40" fill="var(--bg)"/>
    <circle cx="164" cy="81" r="72" fill="var(--bg)"/>
  </svg>

  <div class="brand brand--back"><i></i>Granite Ridge Roofing</div>
  <h1 class="t back-title">Comprehensive<br>Roofing Services</h1>
  <p class="t intro">At Granite Ridge Roofing, we offer a full range of roofing solutions to protect your home:</p>
  <ul class="services">
    <li><span class="ico"><svg width="12" height="12" viewBox="0 0 12 12"><path d="M1 6L6 1.5 11 6M2.5 5v5.5h7V5" stroke="#fff" stroke-width="1.2" fill="none"/></svg></span><span><b>Roof Inspections &amp; Maintenance –</b><br>Keep your roof in peak condition.</span></li>
    <li><span class="ico"><svg width="12" height="12" viewBox="0 0 12 12"><path d="M1 6L6 1.5 11 6M2.5 5v5.5h7V5" stroke="#fff" stroke-width="1.2" fill="none"/></svg></span><span><b>Roof Repairs –</b> Fast, reliable fixes for leaks, storm damage, and more.</span></li>
    <li><span class="ico"><svg width="12" height="12" viewBox="0 0 12 12"><path d="M1 6L6 1.5 11 6M2.5 5v5.5h7V5" stroke="#fff" stroke-width="1.2" fill="none"/></svg></span><span><b>New Roof Installation –</b> Quality materials and expert craftsmanship.</span></li>
    <li><span class="ico"><svg width="12" height="12" viewBox="0 0 12 12"><path d="M1 6L6 1.5 11 6M2.5 5v5.5h7V5" stroke="#fff" stroke-width="1.2" fill="none"/></svg></span><span><b>Storm Damage Repair –</b> Quick response to Arizona's toughest weather.</span></li>
  </ul>

  <h2 class="t contact-title">Contact us:</h2>
  <div class="contact" style="top:694px">
    <svg width="10" height="12" viewBox="0 0 10 12" aria-hidden="true"><path d="M5 0a4 4 0 014 4c0 3-4 8-4 8S1 7 1 4a4 4 0 014-4z" fill="#fff"/><circle cx="5" cy="4" r="1.5" fill="var(--ink)"/></svg>
    214 W Pine Lane Prescott, AZ 86301
  </div>
  <div class="contact" style="top:718px">
    <svg width="10" height="10" viewBox="0 0 10 10" aria-hidden="true"><path d="M1.5 0.5l2 2.2-1 1.3c.7 1.5 1.9 2.7 3.4 3.4l1.3-1 2.2 2-1 1.6C4.5 9.6.4 5.5.1 1.6z" fill="#fff"/></svg>
    (928) 555-0147
    <svg style="margin-left:14px" width="11" height="8" viewBox="0 0 11 8" aria-hidden="true"><rect x="0.5" y="0.5" width="10" height="7" fill="none" stroke="#fff"/><path d="M0.5 0.5l5 4 5-4" stroke="#fff" fill="none"/></svg>
    info@graniteridgeroofing.com
  </div>
  <div class="badges">
    <span class="badge-round"></span>
    <span class="badge-square"></span>
    <span class="roc">AZ ROC 562071</span>
  </div>

  <div class="card-stub"><span>Business card</span></div>
</section>

</body>
</html>
```